Design a Flyer for new years eve

Celebrate (ring in) new years at Vellora Restaurant
Call to make a reservation (415) 382 - 5904

Featuring Daniel Osmer with Acoustic Guitar (nights live entertainment)

Materials could be found
www.velloradining.com
www.facebook.com/velloradining
www.instagram.com/velloradining

Daniel's only picture we have is the one uploaded, feel free to search the web for more if you want.

We want a flyer that is elegant and reflects the ambiance of a classy Mediterranean restaurant.

```html
<!DOCTYPE html>
<html lang="en">
<head>
<meta charset="utf-8">
<title>Vellora Restaurant – New Years 2018</title>
<link href="https://fonts.googleapis.com/css2?family=Josefin+Sans:wght@200;300;400;600&family=Oswald:wght@400;500&family=Roboto:wght@400&display=swap" rel="stylesheet">
<style>
  :root {
    --backdrop: #ececec;
    --ink-dark: #1d1a22;
    --ink-light: #f4f1ec;
    --ink-muted: #d9d6d8;
    --pill: #141217;
    --accent-line: #3aa3d6;
    --glow-cream: #fff6dc;
    --glow-gold: #f3dc9a;
    --sky-violet: #6b4f86;
    --sky-teal: #2f6f86;
    --night: #1a1420;
    --stage-amber: #b8692f;
    --stage-red: #7a2a22;
  }
  * { margin: 0; padding: 0; box-sizing: border-box; }
  html, body { width: 1200px; height: 900px; overflow: hidden; }
  body { background: var(--backdrop); position: relative; }

  .flyer {
    position: absolute;
    left: 278px; top: 30px;
    width: 643px; height: 840px;
    overflow: hidden;
    box-shadow: 0 10px 30px rgba(0,0,0,0.35);
    text-align: center;
  }
  .flyer-photo {
    position: absolute; inset: 0;
    background:
      radial-gradient(ellipse 290px 200px at 50% 250px, var(--glow-cream) 0%, var(--glow-cream) 45%, var(--glow-gold) 62%, rgba(243,220,154,0) 100%),
      radial-gradient(ellipse 420px 260px at 50% 230px, rgba(107,79,134,0.9) 0%, rgba(47,111,134,0.55) 60%, rgba(26,20,32,0) 100%),
      radial-gradient(ellipse 260px 220px at 30% 680px, rgba(184,105,47,0.8) 0%, rgba(122,42,34,0.4) 60%, rgba(26,20,32,0) 100%),
      linear-gradient(180deg, var(--night) 0%, #2a2236 40%, #3a2a2c 65%, var(--night) 100%);
  }

  .brand { position: absolute; top: 104px; left: 0; right: 0; color: var(--ink-dark); }
  .brand-name {
    font-family: 'Josefin Sans', sans-serif; font-weight: 600;
    font-size: 36px; letter-spacing: 5px; line-height: 1;
  }
  .brand-sub {
    margin-top: 8px;
    font-family: 'Josefin Sans', sans-serif; font-weight: 600;
    font-size: 15px; letter-spacing: 4px;
    display: inline-flex; align-items: center; gap: 8px;
  }
  .brand-sub::before, .brand-sub::after {
    content: ""; width: 14px; height: 2px; background: var(--ink-dark);
  }

  .year {
    position: absolute; top: 208px; left: 0; right: 0;
    font-family: 'Josefin Sans', sans-serif; font-weight: 200;
    font-size: 130px; line-height: 1; color: var(--ink-dark); letter-spacing: 2px;
  }
  .celebrate {
    position: absolute; top: 322px; left: 0; right: 0;
    font-family: 'Josefin Sans', sans-serif; font-weight: 300;
    font-size: 20px; letter-spacing: 1px; color: var(--ink-dark);
  }
  .venue {
    position: absolute; top: 345px; left: 0; right: 0;
    font-family: 'Josefin Sans', sans-serif; font-weight: 300;
    font-size: 32px; letter-spacing: 1px; color: var(--ink-dark);
  }

  .featuring {
    position: absolute; top: 460px; left: 50%; transform: translateX(-50%);
    width: 230px; height: 27px;
    background: var(--pill);
    clip-path: polygon(10px 0, calc(100% - 10px) 0, 100% 50%, calc(100% - 10px) 100%, 10px 100%, 0 50%);
    font-family: 'Oswald', sans-serif; font-weight: 400;
    font-size: 16px; letter-spacing: 5px; line-height: 27px; color: var(--ink-light);
  }
  .performer {
    position: absolute; top: 508px; left: 0; right: 0;
    font-family: 'Oswald', sans-serif; font-weight: 500; color: var(--ink-light);
    font-size: 32px; line-height: 1.1;
  }
  .performer-note { font-size: 21px; font-weight: 400; }
  .performer-rule {
    position: absolute; top: 552px; left: 175px; width: 300px; height: 1px;
    background: linear-gradient(90deg, transparent, var(--accent-line), transparent);
  }

  .date-box {
    position: absolute; top: 595px; left: 93px; width: 460px; height: 51px;
    border: 1.5px solid var(--ink-light);
    font-family: 'Oswald', sans-serif; font-weight: 500;
    font-size: 28px; line-height: 48px; color: var(--ink-light); letter-spacing: 0.5px;
  }
  .date-box .stars { font-size: 14px; letter-spacing: 4px; vertical-align: 5px; margin: 0 8px; }
  .date-box sup { font-size: 15px; }

  .reservation {
    position: absolute; top: 706px; left: 0; right: 0;
    font-family: 'Oswald', sans-serif; font-weight: 400;
    font-size: 28px; letter-spacing: 0.5px; color: var(--ink-muted);
  }
  .reservation-rule {
    position: absolute; top: 752px; left: 128px; width: 390px; height: 1px;
    background: linear-gradient(90deg, transparent, var(--accent-line), transparent);
  }

  .links {
    position: absolute; top: 760px; left: 29px;
    list-style: none; text-align: left;
    font-family: 'Roboto', sans-serif; font-size: 14px; line-height: 19px; color: var(--ink-light);
  }
</style>
</head>
<body>
  <article class="flyer">
    <div class="flyer-photo" role="img" aria-label="Fireworks bursting over the night sky above a blurred photo of the guitarist performing on a warmly lit stage"></div>

    <div class="brand">
      <div class="brand-name">VELLORA</div>
      <div class="brand-sub">RESTAURANT</div>
    </div>

    <div class="year">2018</div>
    <div class="celebrate">CELEBRATE NEW YEARS</div>
    <div class="venue">VELLORA RESTAURANT</div>

    <div class="featuring">FEATURING</div>
    <div class="performer">DANIEL OSMER <span class="performer-note">WITH (ACOUSTIC GUITAR)</span></div>
    <div class="performer-rule"></div>

    <div class="date-box"><span class="stars">★★★</span>SUNDAY 31<sup>ST</sup> DECEMBER<span class="stars">★★★</span></div>

    <div class="reservation">RESERVATION: (415) 382 - 5904</div>
    <div class="reservation-rule"></div>

    <ul class="links">
      <li>www.velloradining.com</li>
      <li>www.facebook.com/velloradining</li>
      <li>www.instagram.com/velloradining</li>
    </ul>
  </article>
</body>
</html>
```